Capability Statement Brochure - Corporate

We need to provide our corporate clients with an elegant, professional and well designed capability statement that not only details what our business can offer, but reflects our professionalism with relevant technical photos. I am thinking two pages A 4 pdf will be suitable if the text can fit without looking crowded but happy to extend to 3 or 4 pages if needed . Colours and details can be taken from our website www.quorintech.com.au Some photos have been attached however if we need more professional stock photos I am happy to use them if needed. This project needs to convince potential clients we are the best in industry and our capability is extensive. Please help us relay this to our customers. Thank you,.

Target Market(s)

Corporate, Government, Education, Defence, Healthcare

Industry/Entity Type

Audio Visual Integration

Colors
0054AA
0677BA
7BADD7
CADEEF
E8F1F8

Requirements
Must have
• Style, look classy, sophisticated and technical
Nice to have
• Quorin Tech colours, Logo, website and email and include the PRISM LED Logo
Should not have
• Messy, too much clutter, not easy to read.

```html
<!DOCTYPE html>
<html lang="en">
<head>
<meta charset="utf-8">
<title>Quorin Tech – Capability Statement</title>
<link href="https://fonts.googleapis.com/css2?family=Montserrat:wght@300;400;500;700&display=swap" rel="stylesheet">
<style>
:root{
  --stage:#d3dbee;
  --paper:#ffffff;
  --brand-deep:#0054aa;
  --brand-mid:#0677ba;
  --brand-soft:#7badd7;
  --brand-pale:#cadeef;
  --heading:#5b97d3;
  --body:#6b6f76;
  --rule:#e2e7ee;
  --ink:#2a2d33;
  --accent:#e98a5c;
}
*{box-sizing:border-box;margin:0;padding:0}
html,body{width:1000px;height:1200px;overflow:hidden}
body{background:var(--stage);font-family:"Montserrat",sans-serif;position:relative;color:var(--body)}
.page{position:absolute;width:262px;height:370px;background:var(--paper);box-shadow:0 2px 5px rgba(40,50,80,.18);padding:18px 18px 0}
.p1{left:71px;top:193px;padding:0}
.p2{left:369px;top:193px}
.p3{left:659px;top:193px}
.p4{left:71px;top:619px}
.p5{left:369px;top:619px}
.p6{left:659px;top:619px;padding:0}
.section-title{font-size:9.4px;font-weight:400;color:var(--heading);padding:11px 0 4px;border-bottom:1px solid var(--rule);margin-bottom:6px}
.section-title:first-child{padding-top:3px}
.copy{font-size:5.1px;line-height:6.3px;font-weight:300;padding:0 2px;margin-bottom:6px;color:var(--body)}
.list{list-style:none;font-size:5.1px;line-height:8.1px;font-weight:300;padding:0 2px;margin:8px 0 6px}
.list li::before{content:"· "}
.two-col{display:grid;grid-template-columns:1fr 1fr;margin-top:3px}
.two-col .list{margin:0;line-height:6.4px}
.footer{position:absolute;left:18px;right:18px;top:347px;border-top:1px solid var(--rule);padding-top:3px;display:flex;justify-content:space-between;font-size:5px;font-weight:300}
.wordmark{display:flex;align-items:center;gap:5px;font-weight:500;font-size:12px;color:var(--ink)}
.wordmark .mark{width:10px;height:10px;background:var(--brand-deep)}
.cover-brand{position:absolute;top:40px;left:0;right:0;display:flex;justify-content:center}
.cover-bar{position:absolute;left:23px;width:216px;height:2px;background:var(--brand-soft)}
.photo{position:absolute}
.cover-photo{left:0;top:99px;width:262px;height:204px;background:linear-gradient(180deg,#e4dccb 0%,#cfc2a8 45%,#6d6660 75%,#5a5550 100%)}
.cover-title{position:absolute;top:330px;left:0;right:0;text-align:center}
.cover-title span{font-size:9px;font-weight:400;color:var(--ink);letter-spacing:.2px;padding-bottom:2px;border-bottom:1px solid var(--accent)}
.framed{position:absolute;left:18px;width:225px}
.frame-right{top:275px;height:58px}
.frame-right .edge{position:absolute;left:106px;right:-1px;top:-1px;bottom:-2px;border:2px solid var(--brand-soft);border-left:none}
.frame-right .edge::before{content:"";position:absolute;left:0;bottom:0;width:100%;height:2px;background:var(--brand-soft)}
.lab-photo{position:absolute;inset:0;background:linear-gradient(180deg,#a89a7c 0%,#ddd9d0 45%,#4a4848 100%)}
.prism-badge{position:absolute;left:165px;top:229px;width:78px;text-align:right;font-weight:700;font-size:7px;color:var(--ink);line-height:8px}
.frame-left{top:259px;height:71px}
.frame-left .edge{position:absolute;left:-2px;top:-2px;width:120px;bottom:-2px;border:2px solid var(--brand-soft);border-right:none}
.boardroom-photo{position:absolute;inset:0;background:linear-gradient(180deg,#c4c6c8 0%,#2d4f9c 35%,#8a4a2a 70%,#d3a58a 100%)}
.back-panel{position:absolute;left:19px;top:19px;width:223px;height:284px;background:linear-gradient(160deg,#1d61c2 0%,#0b4fb4 55%,#0a47a6 100%)}
.back-brand{position:absolute;top:146px;left:0;right:0;display:flex;justify-content:center}
.back-brand .wordmark{color:#fff;font-size:12px}
.back-brand .mark{background:#fff}
.contact{position:absolute;top:325px;left:0;right:0;text-align:center;font-size:5.1px;line-height:9px;font-weight:400;color:var(--body)}
.contact-rule{position:absolute;left:19px;right:18px;top:347px;border-top:1px solid var(--rule)}
</style>
</head>
<body>

<section class="page p1">
  <div class="cover-brand"><div class="wordmark"><span class="mark"></span>quorin tech</div></div>
  <div class="cover-bar" style="top:97px"></div>
  <div class="photo cover-photo" role="img" aria-label="Modern boardroom with a long table, white chairs and wall display"></div>
  <div class="cover-bar" style="top:304px"></div>
  <div class="cover-title"><span>CAPABILITY STATEMENT</span></div>
</section>

<section class="page p2">
  <h2 class="section-title">Company Overview</h2>
  <p class="copy">Quorin Tech (QTS) is a leading Australian audiovisual integration specialist delivering advanced AV, unified communications, collaboration environments, and large-scale digital display systems across Australia.</p>
  <p class="copy">With more than 26 years of industry experience, QTS provides end-to-end services including system design, engineering, installation, commissioning, and long-term technical support. Our solutions enable organisations to communicate, collaborate, and share information effectively across boardrooms, control centres, training environments, operational facilities, and large public spaces.</p>
  <p class="copy">QTS works across a broad range of sectors including healthcare, corporate enterprise, government, defence, mining and resources, and education. Our team combines deep technical expertise with a strong understanding of operational environments where reliability, security, and ease of use are essential.</p>
  <h2 class="section-title">Core Capabilities</h2>
  <ul class="list">
    <li>AV System Design and Engineering</li>
    <li>Unified Communications and Collaboration Systems</li>
    <li>LED Video Walls and Large Format Displays</li>
    <li>Control Rooms and Operations Centres</li>
    <li>Boardrooms and Executive Meeting Spaces</li>
    <li>Education and Training Environments</li>
    <li>Digital Signage and Information Display Networks</li>
    <li>AV over IP and Networked Media Systems</li>
    <li>System Programming, Automation and Control</li>
    <li>Ongoing Service, Maintenance and Technical Support</li>
  </ul>
  <div class="framed frame-right">
    <div class="edge"></div>
    <div class="lab-photo" role="img" aria-label="Computer training room with rows of monitors on desks"></div>
  </div>
  <div class="footer"><span>www.quorintech.com.au</span><span>02</span></div>
</section>

<section class="page p3">
  <h2 class="section-title">LED Video Wall Expertise</h2>
  <p class="copy">Quorin Tech has extensive experience designing and installing direct-view LED video walls for corporate environments, education facilities, public venues, and large presentation spaces.</p>
  <p class="copy">Our proprietary PRISM LED video wall solutions provide exceptional brightness, durability, and reliability for high-impact display environments such as school halls, gymnasiums, corporate auditoriums, and public venues.</p>
  <p class="copy">QTS provides complete LED video wall solutions including structural design, engineering certification, installation, commissioning, and ongoing support.</p>
  <h2 class="section-title">Markets Served</h2>
  <div class="two-col">
    <ul class="list"><li>Healthcare</li><li>Corporate &amp; Enterprise</li><li>Government</li><li>Defence</li></ul>
    <ul class="list"><li>Mining &amp; Resources</li><li>Education</li><li>Public Venues and Event Spaces</li></ul>
  </div>
  <h2 class="section-title">Healthcare Experience</h2>
  <p class="copy">QTS has extensive experience delivering audiovisual solutions within major healthcare environments including clinical communication systems, specialist consultation rooms, training facilities, and hospital-wide digital signage networks.</p>
  <p class="copy">For over 20 years QTS has supported Harbourside General Hospital with the design, implementation, and support of audiovisual infrastructure across departments including ICU, Emergency, Cardiology, Radiology, and Allied Health.</p>
  <h2 class="section-title">Corporate &amp; Enterprise</h2>
  <p class="copy">QTS delivers modern collaboration environments that enable organisations to connect teams across offices, remote staff, and global partners.</p>
  <p class="copy">Solutions include boardrooms, hybrid meeting rooms, training facilities, corporate digital signage networks, and executive collaboration spaces.</p>
  <div class="footer"><span>www.quorintech.com.au</span><span>03</span></div>
</section>

<section class="page p4">
  <h2 class="section-title">Government &amp; Defence</h2>
  <p class="copy">QTS supports government departments and defence organisations with reliable and secure audiovisual systems designed for operational environments including command centres, training facilities, situation rooms, and secure conferencing spaces.</p>
  <h2 class="section-title">Mining &amp; Resources</h2>
  <p class="copy">QTS provides robust AV systems designed for industrial and remote environments including operations centres, training rooms, induction facilities, and remote collaboration systems supporting mining and energy sector operations.</p>
  <h2 class="section-title">Education</h2>
  <p class="copy">QTS delivers innovative AV solutions for schools, universities, and training institutions including lecture theatres, classrooms, hybrid learning environments, school halls, gymnasiums, and large-scale LED display systems.</p>
  <h2 class="section-title">Design &amp; Engineering</h2>
  <p class="copy">QTS provides comprehensive in-house design and engineering services including system architecture, documentation, schematics, networked AV design, and integration with existing IT infrastructure.</p>
  <p class="copy">Our team works closely with architects, consultants, builders, and project managers to ensure seamless integration of audiovisual technology within new builds and refurbishment projects.</p>
  <h2 class="section-title">Implementation &amp; Commissioning</h2>
  <p class="copy">QTS delivers complete turnkey project implementation including equipment procurement, professional installation, system configuration, testing, commissioning, and user training.</p>
  <p class="copy">Our accredited technicians ensure systems are delivered safely, efficiently, and with minimal disruption to operational environments.</p>
  <div class="footer"><span>www.quorintech.com.au</span><span>04</span></div>
</section>

<section class="page p5">
  <h2 class="section-title">Service &amp; Support</h2>
  <p class="copy">QTS provides comprehensive ongoing support services including preventative maintenance, priority service response, remote diagnostics, system upgrades, and technology lifecycle planning.</p>
  <p class="copy">Our long-term support partnerships ensure systems remain reliable, secure, and aligned with evolving organisational needs.</p>
  <h2 class="section-title">Governance, Safety &amp; Compliance</h2>
  <p class="copy">QTS operates under strict safety and governance frameworks including OH&amp;S compliant work practices, industry-certified technicians, and full public liability and professional indemnity coverage.</p>
  <p class="copy">Safety, compliance, and quality assurance are embedded throughout all project delivery activities.</p>
  <h2 class="section-title" style="padding-top:14px">Why Choose Quorin Tech</h2>
  <ul class="list">
    <li>26+ years audiovisual integration experience</li>
    <li>Proven track record across multiple industries</li>
    <li>In-house design and engineering capability</li>
    <li>National project delivery capability</li>
    <li>LED video wall specialists</li>
    <li>Long-term service and support partnerships</li>
  </ul>
  <div class="prism-badge">PRISM<br>LED VIDEO WALL</div>
  <div class="framed frame-left">
    <div class="edge"></div>
    <div class="boardroom-photo" role="img" aria-label="Conference table with a row of microphones and blue chairs"></div>
  </div>
  <div class="footer"><span>www.quorintech.com.au</span><span>05</span></div>
</section>

<section class="page p6">
  <div class="back-panel" role="img" aria-label="Blue-toned photo of technicians working in a laboratory"></div>
  <div class="back-brand"><div class="wordmark"><span class="mark"></span>quorin tech</div></div>
  <div class="contact">1300 555 014<br>info@quorintech.com.au &nbsp;&nbsp;|&nbsp;&nbsp; www.quorintech.com.au</div>
  <div class="contact-rule"></div>
</section>

</body>
</html>
```